Suchen ansprechendes & seriöses Urkunden/Zertifikat Design für Webseite & Druck
Zielgruppe
Auf unserer Webseite http://rege-im-alter-netz.de können sich Unternehmen, Institutionen und Vereine ihre Seniorenfreundlichkeit durch ein Zertifikat bestätigen und zertifizieren lassen.
Unsere Kundengruppen: Hotel – Gastronomie – Wellness – Reisen und Touristik – Touristikregionen – Seniorenshop – Onlineshop – Unternehmen als Dienstleister – Medizin und Health-Service – Apotheke – Altenheim – Pflegeheim – Seniorenheim – Vereine – Seniorenservice – Zahnärzte – Fitnessstudio – Sportstudio – Physiotherapie – Sportverein – Golfclub – und viele weitere seniorenfreundliche Institutionen.
Aufgabenstellung
Auftrag- Ausschreibung:
- Erstellung eines Design:
- Urkunde für Webseite rege-im-alter-netz.de - Das Zertifikat "Rege im Alter“
Funktion:
Kunde erkennt das Zertifikat - Logo auf einer Webseite und Klickt auf dieses.
Er wird weitergeleitet auf eine Unterseite, worin die Richtlinien und die Urkunde sichtbar wird.
Zielgruppe:
- Unternehmen, welche das Zertifikat auf Ihre Webseite setzen. Die Urkunde gibt Auskunft, dass der Dienstleister einen besonderen Service für Senioren ausübt. Die Urkunde ist sichtbar auf der Webseite, indem das Logo angeklickt wird. Die Urkunde gibt es ebenfalls als Download, damit der Kunde diese in seinen Geschäftsräumen aufhängen kann oder diese in seinen Werbeunterlagen präsentieren kann.
- Verbraucher sollen beeindruckt sein, von der Urkunde, welches Vertrauen ausstrahlt, aber auch Seriosität
Folgende Ausstrahlung soll die Urkunde haben:
- Soll Mitbewerber des Zertifikatsinhaber beeindrucken und das Verlangen aufzeigen, sich ebenfalls zertifizieren zu lassen ( ca: 70% der Kunden sind Mitbewerber … ). Nach dem Motto "Das Logo ist super und edel, das muss ich auch haben!"
- Der Kunde als Verbraucher soll Vertrauen gewinnen, die Daten sollen gut sichtbar sein, aber nicht verkitscht wie eine Urkunde bei einer Kaffeefahrt. Der Verbraucher geht auf das Zertifikat und kommt zur Urkunde, deshalb soll die Farbe, und Darstellung, Seriosität des Unternehmens ausstrahlen.
Sonstiges
- Die Urkunde soll dem neuen Design unserer Seite (zu sehen unter: http://guetesiegel-welt.de) angepasst sein.
- Vor Auftragsendvergabe erhalten Sie noch ein telefonisches Briefing über unsere Erfahrungswerte
Link zur bestehenden alten Webseite (Altes Design): http://rege-im-alter-netz.de
Info Verbraucher: http://www.rege-im-alter-netz.de/verbraucher/
Info zum Zertifikat: http://www.rege-im-alter-ne..

```html
<!DOCTYPE html>
<html lang="de">
<head>
<meta charset="utf-8">
<title>Zertifikat – Rege im Alter</title>
<link rel="stylesheet" href="https://fonts.googleapis.com/css2?family=Bebas+Neue&family=Montserrat:wght@300;400;700&display=swap">
<style>
  :root {
    --paper: #ffffff;
    --paper-tint: #f6f2ee;
    --brand-red: #b8282a;
    --ink: #1c1c1c;
    --frame: #c9ab8c;
    --seal-grey: #c8c8c8;
    --seal-ring: #9e1f24;
  }
  * { margin: 0; padding: 0; box-sizing: border-box; }
  html, body { width: 850px; height: 1200px; overflow: hidden; background: var(--paper); }
  .certificate {
    position: relative; width: 850px; height: 1200px;
    background: var(--paper);
    font-family: "Montserrat", sans-serif; color: var(--ink);
  }
  .certificate__field {
    position: absolute; left: 70px; top: 68px; width: 710px; height: 1057px;
    background: var(--paper-tint);
    border: 3px solid var(--frame);
    outline: 1px solid var(--frame); outline-offset: 6px;
  }
  .certificate__title {
    position: absolute; left: 0; width: 850px; top: 92px; text-align: center;
    font-family: "Bebas Neue", sans-serif; font-size: 178px; line-height: 1;
    color: var(--brand-red); letter-spacing: 2px;
  }
  .certificate__subtitle {
    position: absolute; left: 0; width: 850px; top: 240px; text-align: center;
    font-weight: 300; font-size: 56px; letter-spacing: 1px; color: var(--ink);
  }
  .details { position: absolute; left: 0; top: 332px; width: 850px; }
  .details__row { display: flex; margin-bottom: 28px; font-size: 22px; line-height: 30px; }
  .details__row--tight { margin-bottom: 8px; }
  .details__label { width: 350px; text-align: right; font-weight: 700; padding-right: 10px; }
  .details__value { font-weight: 300; }
  .confirmation {
    position: absolute; left: 188px; top: 922px; font-size: 22px; font-weight: 700;
  }
  .signature { position: absolute; top: 968px; height: 76px; }
  .signature--first { left: 148px; width: 150px; }
  .signature--second { left: 298px; width: 170px; }
  .signature__mark { width: 100%; height: 56px; background: linear-gradient(90deg, transparent, #e4e0dc 20%, #e4e0dc 80%, transparent); }
  .signature__name { font-size: 18px; font-weight: 300; text-align: center; margin-top: 2px; }
  .seal { position: absolute; left: 478px; top: 910px; width: 230px; height: 230px; }
  .seal__name {
    position: absolute; left: 478px; top: 1144px; width: 230px; text-align: center;
    font-size: 22px; font-weight: 700; color: var(--brand-red);
  }
  .page-number { position: absolute; left: 14px; top: 1168px; font-size: 22px; font-weight: 700; }
</style>
</head>
<body>
<main class="certificate">
  <div class="certificate__field"></div>

  <h1 class="certificate__title">Zertifikat</h1>
  <p class="certificate__subtitle">REGE IM ALTER</p>

  <section class="details">
    <div class="details__row"><span class="details__label">Zertifikat ID:</span><span class="details__value">7250441e9e</span></div>
    <div class="details__row"><span class="details__label">Anbieter:</span><span class="details__value">Rege im Alter<br>Ihr Zertifizierungsdienst</span></div>
    <div class="details__row"><span class="details__label">Status:</span><span class="details__value">aktiv</span></div>
    <div class="details__row"><span class="details__label">Unternehmen:</span><span class="details__value">Seniorenhilfe Linde<br>Ahornweg 7<br>54321 Musterort<br>Deutschland<br>kontakt@linde-hilfe.org</span></div>
    <div class="details__row"><span class="details__label">Vertretungs-<br>berechtigter:</span><span class="details__value">Frau Helga<br>Linde</span></div>
    <div class="details__row details__row--tight"><span class="details__label">Erstprüfung am:</span><span class="details__value">07.04.2017</span></div>
    <div class="details__row"><span class="details__label">gültig bis:</span><span class="details__value">07.04.2019</span></div>
  </section>

  <p class="confirmation">Bestätigt von:</p>

  <div class="signature signature--first">
    <div class="signature__mark" role="img" aria-label="Handschriftliche Unterschrift K. Vogt"></div>
    <p class="signature__name">K. Vogt</p>
  </div>
  <div class="signature signature--second">
    <div class="signature__mark" role="img" aria-label="Handschriftliche Unterschrift L. Brandt"></div>
    <p class="signature__name">L. Brandt</p>
  </div>

  <svg class="seal" viewBox="0 0 230 230" aria-hidden="true">
    <circle cx="115" cy="115" r="108" fill="var(--seal-grey)" stroke="var(--seal-ring)" stroke-width="10"/>
  </svg>
  <p class="seal__name">Rege im Alter</p>

  <span class="page-number">20</span>
</main>
</body>
</html>
```